Kobalto Cell Phone Repair

We are a small cell phone repair store in need of a redesign to our current business card to make it a more modern, cleaner design that will catch folks' attention (perhaps with rounded edges ) - But still include most of the information listed on the current card. Would like to keep the current color scheme of black/white and green. Card will not need any personnel name included. Would like to see some designs include takes on a velorin or tekvo screen as well as more traditional cards.

Target Market(s)

broad spectrum across all cell phone users

Industry/Entity Type

Cell Phone

Contact Information for Business Card

changes to front text:
keep business Logo
business address, phone number website and email. All other info optional (add gathernest and blurvo icons on card

Rear of card:

Keep repair services, change tekvo repair to slatra repair, change quorvex os repair to data recovery (with appropriate icon or substitute)
remove products text
remove pjw and ravesh from manufacturer logos, add dunbelio.

Requirements
Must have
• business Logo
• business address, phone number website and email
• keep colors to white/black/green/gray
• gathernest and blurvo icons on card
Nice to have
• Would like to see 'traditional' business card design as well as creative design incorporating incorporating front of cell phone (eg tekvo or quorvex). Rounded edges would be nice but not necessary.

```html
<!DOCTYPE html>
<html lang="en">
<head>
<meta charset="utf-8">
<title>Kobalto Cell Phone Repair – Business Card</title>
<link href="https://fonts.googleapis.com/css2?family=Rubik:wght@400;500;700&display=swap" rel="stylesheet">
<style>
  :root {
    --green: #62ad46;
    --green-dark: #44872f;
    --ink: #2e2e30;
    --gray: #999a9c;
    --label: #8a8a8a;
    --white: #ffffff;
  }
  * { margin: 0; padding: 0; box-sizing: border-box; }
  html, body { width: 1200px; height: 994px; overflow: hidden; background: var(--white); }
  body { position: relative; font-family: "Rubik", Arial, sans-serif; }

  .card { position: absolute; left: 0; top: 0; width: 829px; height: 994px; }

  /* Front */
  .front { position: absolute; left: 0; top: 0; width: 829px; height: 367px; background: var(--white); }
  .brand { position: absolute; left: 0; width: 829px; top: 12px; text-align: center; }
  .brand-name { font-size: 48px; font-weight: 700; color: var(--green); letter-spacing: -1px; line-height: 1; }
  .brand-tag { font-size: 20px; font-weight: 400; color: var(--green); margin-top: 4px; }
  .service-list { position: absolute; left: 0; width: 829px; top: 126px; text-align: center; list-style: none; }
  .service-list li { font-size: 33px; font-weight: 500; color: var(--gray); line-height: 40px; letter-spacing: -0.5px; }
  .mascot { position: absolute; left: 692px; top: 71px; width: 137px; height: 240px; border-radius: 40px 0 0 20px;
            background: linear-gradient(160deg, #8fd06a, #56a63a); }
  .rule-dark { position: absolute; left: 0; top: 310px; width: 829px; height: 8px; background: var(--ink); }
  .band-green { position: absolute; left: 0; top: 318px; width: 829px; height: 49px; background: var(--green); }

  /* Contact strip */
  .contact { position: absolute; left: 0; top: 367px; width: 829px; height: 131px; background: var(--white); color: var(--ink); }
  .contact-row { position: absolute; left: 0; width: 829px; display: flex; justify-content: center; align-items: center; gap: 18px; }
  .contact-row span { display: inline-flex; align-items: center; gap: 5px; }
  .row-address { top: 18px; font-size: 20px; font-weight: 500; letter-spacing: -0.4px; }
  .row-web { top: 50px; font-size: 18px; font-weight: 500; letter-spacing: -0.3px; }
  .row-social { top: 80px; font-size: 18px; font-weight: 500; gap: 12px; }
  .ico { width: 18px; height: 18px; fill: var(--green); }
  .dot { width: 14px; height: 14px; border-radius: 50%; background: var(--green); display: inline-block; }

  /* Back */
  .back { position: absolute; left: 0; top: 498px; width: 829px; height: 496px; background: var(--green); color: var(--white); }
  .back-title { position: absolute; top: 50px; width: 829px; text-align: center; font-size: 29px; font-weight: 700; letter-spacing: -0.6px; }
  .repair-grid { position: absolute; top: 108px; left: 67px; display: flex; gap: 39.5px; list-style: none; }
  .repair-item { width: 83px; text-align: center; }
  .repair-thumb { width: 83px; height: 83px; border-radius: 8px; border: 1px solid rgba(255,255,255,0.6); }
  .repair-name { font-size: 17px; font-weight: 500; line-height: 22px; margin-top: 6px; margin-left: -30px; margin-right: -30px; }
  .t-screen { background: linear-gradient(135deg, #3a3a3a, #111); }
  .t-water { background: linear-gradient(180deg, #2aa6e0, #0d5f8f); }
  .t-port { background: linear-gradient(180deg, #f4f4f4, #d6a794); }
  .t-data { background: radial-gradient(circle, #5ed8ff, #0b3f9c); }
  .t-unlock { background: linear-gradient(180deg, #ffffff, #cfcfcf); }
  .t-slatra { background: linear-gradient(180deg, #f2f2f2, #d9d9d9); }
  .divider { position: absolute; top: 336px; left: 83px; width: 667px; height: 2px;
             background: linear-gradient(90deg, transparent, rgba(255,255,255,0.85), transparent); }
  .maker-box { position: absolute; top: 354px; left: 65px; width: 699px; height: 96px; border-radius: 8px;
               background: var(--green-dark); display: flex; justify-content: center; align-items: center; gap: 40px; }
  .maker { font-size: 20px; font-weight: 700; color: var(--white); }

  /* Labels */
  .side-label { position: absolute; left: 933px; font-size: 68px; font-weight: 500; color: var(--label); letter-spacing: -1px; line-height: 1; }
  .label-front { top: 214px; }
  .label-back { top: 713px; }
</style>
</head>
<body>
<main class="card">
  <section class="front">
    <div class="brand">
      <div class="brand-name">KOBALTO</div>
      <div class="brand-tag">Cell Phone Repair</div>
    </div>
    <ul class="service-list">
      <li>Unlocking &amp; Flashing Services</li>
      <li>Smart Phones &amp; Accessories</li>
      <li>Water Damage Repair</li>
      <li>Screen Repair</li>
    </ul>
    <div class="mascot" role="img" aria-label="Waving green cartoon lizard mascot"></div>
    <div class="rule-dark"></div>
    <div class="band-green"></div>
  </section>

  <section class="contact">
    <div class="contact-row row-address">
      <span><svg class="ico" viewBox="0 0 24 24"><path d="M12 2a7 7 0 0 0-7 7c0 5 7 13 7 13s7-8 7-13a7 7 0 0 0-7-7zm0 10a3 3 0 1 1 0-6 3 3 0 0 1 0 6z"/></svg>418 Harbor Row, Millbrook MD 20917</span>
    </div>
    <div class="contact-row row-web">
      <span><svg class="ico" viewBox="0 0 24 24"><circle cx="12" cy="12" r="9" fill="none" stroke="#62ad46" stroke-width="2.4"/><path d="M3 12h18M12 3c3 3 3 15 0 18M12 3c-3 3-3 15 0 18" fill="none" stroke="#62ad46" stroke-width="1.8"/></svg>www.kobaltorepair.com</span>
      <span><svg class="ico" viewBox="0 0 24 24"><rect x="2" y="5" width="20" height="14" rx="1" fill="none" stroke="#62ad46" stroke-width="2"/><path d="M2 6l10 7 10-7" fill="none" stroke="#62ad46" stroke-width="2"/></svg>hello@kobaltorepair.com</span>
      <span><svg class="ico" viewBox="0 0 24 24"><path d="M6.6 10.8a15 15 0 0 0 6.6 6.6l2.2-2.2c.3-.3.7-.4 1-.2 1.1.4 2.3.6 3.6.6.6 0 1 .4 1 1V20c0 .6-.4 1-1 1A17 17 0 0 1 3 4c0-.6.4-1 1-1h3.5c.6 0 1 .4 1 1 0 1.3.2 2.5.6 3.6.1.3 0 .7-.2 1z"/></svg>555 014 2760</span>
    </div>
    <div class="contact-row row-social">
      <span><i class="dot"></i>blurvo</span>
      <span><i class="dot"></i>gathernest</span>
    </div>
  </section>

  <section class="back">
    <h2 class="back-title">Cell Phone Repair Services</h2>
    <ul class="repair-grid">
      <li class="repair-item"><div class="repair-thumb t-screen" role="img" aria-label="Photo of a cracked phone screen"></div><div class="repair-name">Screen<br>Repair</div></li>
      <li class="repair-item"><div class="repair-thumb t-water" role="img" aria-label="Photo of a phone splashing into water"></div><div class="repair-name">Water<br>Damage</div></li>
      <li class="repair-item"><div class="repair-thumb t-port" role="img" aria-label="Photo of a phone charging port held in hand"></div><div class="repair-name">Charging Port<br>Repair</div></li>
      <li class="repair-item"><div class="repair-thumb t-data" role="img" aria-label="Digital circuit illustration with a folder for data recovery"></div><div class="repair-name">Data<br>Recovery</div></li>
      <li class="repair-item"><div class="repair-thumb t-unlock" role="img" aria-label="Photo of a phone with a key and lock"></div><div class="repair-name">Cell Phone<br>Unlock</div></li>
      <li class="repair-item"><div class="repair-thumb t-slatra" role="img" aria-label="Photo of a slatra tablet with beach wallpaper"></div><div class="repair-name">slatra<br>Repair</div></li>
    </ul>
    <div class="divider"></div>
    <div class="maker-box">
      <span class="maker">Pomaro</span>
      <span class="maker">velorin</span>
      <span class="maker">Brambek</span>
      <span class="maker">Elgon</span>
      <span class="maker">dunbelio</span>
    </div>
  </section>
</main>

<div class="side-label label-front">Front</div>
<div class="side-label label-back">Back</div>
</body>
</html>
```